K7R Business Cards

Business Cards

Contact Information for Business Card

Company name, owner name, license #s, phone & email

Requirements
Should not have
• mailing address

```html
<!DOCTYPE html>
<html lang="en">
<head>
<meta charset="utf-8">
<title>K7R Construction Business Cards</title>
<link rel="stylesheet" href="https://fonts.googleapis.com/css2?family=Lato:wght@400;700;900&display=swap">
<style>
  :root {
    --bg: #1f1f22;
    --card-white: #ffffff;
    --brand-blue: #0a3aa0;
    --brand-red: #c8101a;
    --ink: #1a1a1a;
    --ink-soft: #333333;
  }
  * { margin: 0; padding: 0; box-sizing: border-box; }
  html, body {
    width: 1200px; height: 718px; overflow: hidden;
    background: var(--bg);
    font-family: "Lato", Arial, sans-serif;
  }
  .stage {
    position: relative; width: 1200px; height: 718px;
    display: flex; align-items: center; justify-content: center; gap: 40px;
  }
  .card {
    position: relative; width: 540px; height: 309px;
    border-radius: 22px; overflow: hidden;
    box-shadow: 0 14px 30px rgba(0,0,0,.45);
  }
  /* Front */
  .card--front { background: var(--card-white); }
  .front-wordmark {
    position: absolute; top: 46px; left: 0; right: 0;
    text-align: center; color: var(--brand-blue);
    font-weight: 900; line-height: 1;
  }
  .front-wordmark .mark-main { display: block; font-size: 78px; letter-spacing: 2px; }
  .front-wordmark .mark-sub { display: block; font-size: 27px; letter-spacing: 1px; margin-top: 2px; }
  .identity {
    position: absolute; left: 70px; top: 190px; width: 200px; text-align: right;
  }
  .identity .person-name {
    color: var(--brand-blue); font-weight: 900; font-size: 25px; letter-spacing: .5px; line-height: 1;
  }
  .identity .license {
    color: var(--brand-red); font-size: 14px; margin-top: 4px;
  }
  .divider {
    position: absolute; left: 290px; top: 180px; width: 2px; height: 58px; background: var(--brand-blue);
  }
  .contact {
    position: absolute; left: 306px; top: 184px; list-style: none;
  }
  .contact li { display: flex; align-items: center; gap: 8px; color: var(--ink-soft); }
  .contact .phone { font-size: 20px; letter-spacing: .5px; margin-bottom: 8px; }
  .contact .email { font-size: 14px; }
  .contact svg { flex: none; }
  .front-stripe { position: absolute; left: 0; bottom: 0; width: 540px; height: 42px; }
  /* Back */
  .card--back { background: var(--brand-blue); }
  .back-wordmark {
    position: absolute; left: 32px; top: 118px; width: 250px;
    text-align: center; color: var(--card-white); font-weight: 900; line-height: 1;
  }
  .back-wordmark .mark-main { display: block; font-size: 74px; letter-spacing: 2px; }
  .back-wordmark .mark-sub { display: block; font-size: 25px; letter-spacing: 1px; margin-top: 2px; }
  .portrait {
    position: absolute; right: 0; bottom: 0; width: 215px; height: 289px;
    background: linear-gradient(180deg, #2a3a78 0%, #3a3a44 45%, #1f1f24 100%);
    border-top-left-radius: 90px 110px;
  }
</style>
</head>
<body>
<main class="stage">
  <section class="card card--front" aria-label="Business card front">
    <div class="front-wordmark">
      <span class="mark-main">K7R</span>
      <span class="mark-sub">CONSTRUCTION</span>
    </div>
    <div class="identity">
      <p class="person-name">DANA WHITLOCK</p>
      <p class="license">MN Lic #BC482615</p>
    </div>
    <div class="divider"></div>
    <ul class="contact">
      <li class="phone">
        <svg width="16" height="16" viewBox="0 0 24 24" aria-hidden="true"><path fill="var(--brand-red)" d="M6.6 10.8a15 15 0 0 0 6.6 6.6l2.2-2.2a1 1 0 0 1 1-.25 11.4 11.4 0 0 0 3.6.6 1 1 0 0 1 1 1V20a1 1 0 0 1-1 1A17 17 0 0 1 3 4a1 1 0 0 1 1-1h3.5a1 1 0 0 1 1 1c0 1.25.2 2.45.6 3.6a1 1 0 0 1-.25 1z"/></svg>
        612-555-0147
      </li>
      <li class="email">
        <svg width="16" height="12" viewBox="0 0 24 18" aria-hidden="true"><rect width="24" height="18" fill="var(--brand-red)"/><path d="M1 1l11 9 11-9" fill="none" stroke="#fff" stroke-width="2"/></svg>
        dwhitlock@mailbox.com
      </li>
    </ul>
    <svg class="front-stripe" viewBox="0 0 540 42" preserveAspectRatio="none" aria-hidden="true">
      <polygon points="0,42 540,42 540,8 0,34" fill="var(--brand-blue)"/>
      <polygon points="365,22 540,0 540,10 360,32" fill="var(--card-white)"/>
      <polygon points="372,22 540,0 540,12 367,34" fill="var(--brand-red)"/>
      <polygon points="0,34 540,8 540,42 0,42" fill="var(--brand-blue)" opacity="0"/>
    </svg>
  </section>

  <section class="card card--back" aria-label="Business card back">
    <div class="back-wordmark">
      <span class="mark-main">K7R</span>
      <span class="mark-sub">CONSTRUCTION</span>
    </div>
    <div class="portrait" role="img" aria-label="Portrait photo of the owner in a dark suit"></div>
  </section>
</main>
</body>
</html>
```